Road Construction Company needs business cards

We would like a new business card designed for our business.

We're a road construction company based in Qld, Australia.

Can the business card please have the following information on it.

Name: Brent Malvoy
Position: General Manager
Phone: 0471 592 304
Email: Brent.malvoy@quendix.com.au
Address: 87 Harrowgate Ave, Pindarra, QLD, 4000
Website: www.quendix.com.au

Visually we'd like the card to be professional and simple.

Attached is our logo.

Our website is www.quendix.com.au

Target Market(s)

Men aged 25-60

Contact Information for Business Card

As listed in project description

Font styles to use
Serif

Requirements
Must have
• Large logo on back of card

```html
<!DOCTYPE html>
<html lang="en">
<head>
<meta charset="utf-8">
<title>Quendix Business Card</title>
<link rel="stylesheet" href="https://fonts.googleapis.com/css2?family=Tinos:wght@400;700&display=swap">
<style>
  :root {
    --page-bg: #e4e4e4;
    --navy-top: #2c4768;
    --navy-bottom: #172c4a;
    --stripe-blue: #36659c;
    --text-white: #ffffff;
    --text-silver: #b4bcc6;
    --icon-silver: #9aa4b0;
    --brand-blue: #2461b0;
    --back-light: #ffffff;
    --back-mid: #b4b6c3;
    --back-dark: #7d8298;
    --facet-dark: #66708e;
  }
  * { margin: 0; padding: 0; box-sizing: border-box; }
  html, body {
    width: 1200px;
    height: 900px;
    overflow: hidden;
    background: var(--page-bg);
    font-family: "Tinos", "Times New Roman", serif;
  }
  .card-row {
    position: absolute;
    top: 296px;
    left: 40px;
    display: flex;
    gap: 40px;
  }
  .card {
    position: relative;
    width: 540px;
    height: 308px;
    overflow: hidden;
  }

  /* Front */
  .card-front {
    background: linear-gradient(180deg, var(--navy-top) 0%, var(--navy-bottom) 100%);
    color: var(--text-white);
  }
  .holder {
    position: absolute;
    top: 86px;
    left: 0;
    width: 100%;
    text-align: center;
  }
  .holder-name {
    font-weight: 700;
    font-size: 29px;
    letter-spacing: 0.5px;
    line-height: 1.05;
  }
  .holder-role {
    font-size: 20px;
    color: var(--text-silver);
    line-height: 1.2;
  }
  .contact-list {
    position: absolute;
    left: 22px;
    top: 204px;
    list-style: none;
  }
  .contact-item {
    display: flex;
    align-items: center;
    gap: 8px;
    font-size: 14.5px;
    height: 23.5px;
  }
  .contact-icon {
    width: 15px;
    height: 15px;
    flex: none;
  }
  .front-brand {
    position: absolute;
    right: 18px;
    top: 222px;
    text-align: left;
    color: var(--text-silver);
  }
  .front-brand-name {
    font-weight: 700;
    font-size: 22px;
    letter-spacing: 2px;
    line-height: 1;
  }
  .front-brand-web {
    font-weight: 700;
    font-size: 11.5px;
    margin-top: 6px;
  }
  .stripe {
    position: absolute;
    left: 0;
    width: 100%;
    background: var(--stripe-blue);
  }
  .stripe-upper { top: 279px; height: 6px; }
  .stripe-lower { top: 292px; height: 8px; }

  /* Back */
  .card-back {
    background: linear-gradient(90deg, var(--back-light) 12%, var(--back-mid) 60%, var(--back-dark) 100%);
  }
  .back-facets {
    position: absolute;
    inset: 0;
    width: 100%;
    height: 100%;
  }
  .back-brand {
    position: absolute;
    top: 0;
    left: 0;
    width: 100%;
    height: 100%;
    display: flex;
    align-items: center;
    justify-content: center;
    padding-left: 6px;
    font-weight: 700;
    font-size: 60px;
    letter-spacing: 3px;
    color: var(--brand-blue);
  }
</style>
</head>
<body>
  <main class="card-row">
    <section class="card card-front" aria-label="Business card front">
      <div class="holder">
        <h1 class="holder-name">BRENT MALVOY</h1>
        <p class="holder-role">General Manager</p>
      </div>

      <ul class="contact-list">
        <li class="contact-item">
          <svg class="contact-icon" viewBox="0 0 16 16" aria-hidden="true">
            <path d="M3.5 1.5l2.5 3-1.5 1.8c.8 1.8 2.3 3.3 4.2 4.2l1.8-1.5 3 2.5-1.4 2C7 13.2 2.8 9 1.5 3z" fill="none" stroke="var(--icon-silver)" stroke-width="1.2" stroke-linejoin="round"/>
          </svg>
          <span>0471 592 304</span>
        </li>
        <li class="contact-item">
          <svg class="contact-icon" viewBox="0 0 16 16" aria-hidden="true">
            <circle cx="8" cy="8" r="6.8" fill="none" stroke="var(--icon-silver)" stroke-width="1.1"/>
            <circle cx="8" cy="8" r="2.4" fill="none" stroke="var(--icon-silver)" stroke-width="1.1"/>
            <path d="M10.4 5.8v3.2c0 1.2 1.8 1.2 1.8-.4" fill="none" stroke="var(--icon-silver)" stroke-width="1.1"/>
          </svg>
          <span>Brent.malvoy@quendix.com.au</span>
        </li>
        <li class="contact-item">
          <svg class="contact-icon" viewBox="0 0 16 16" aria-hidden="true">
            <path d="M8 15s-5-5.2-5-8.6a5 5 0 0110 0C13 9.8 8 15 8 15z" fill="none" stroke="var(--icon-silver)" stroke-width="1.2"/>
            <circle cx="8" cy="6.4" r="1.8" fill="var(--icon-silver)"/>
          </svg>
          <span>87 Harrowgate Ave, Pindarra, QLD, 4000</span>
        </li>
      </ul>

      <div class="front-brand">
        <p class="front-brand-name">QUENDIX</p>
        <p class="front-brand-web">www.quendix.com.au</p>
      </div>

      <div class="stripe stripe-upper"></div>
      <div class="stripe stripe-lower"></div>
    </section>

    <section class="card card-back" aria-label="Business card back">
      <svg class="back-facets" viewBox="0 0 540 308" preserveAspectRatio="none" aria-hidden="true">
        <defs>
          <linearGradient id="facet-fade" x1="0" y1="0" x2="1" y2="0">
            <stop offset="0" stop-color="#ffffff" stop-opacity="0"/>
            <stop offset="1" stop-color="var(--facet-dark)" stop-opacity="0.55"/>
          </linearGradient>
        </defs>
        <polygon points="340,0 178,300 540,300 540,0" fill="url(#facet-fade)" opacity="0.35"/>
        <polygon points="462,0 540,0 540,140" fill="var(--facet-dark)" opacity="0.25"/>
        <polygon points="400,150 540,240 540,308 180,308" fill="#ffffff" opacity="0.18"/>
      </svg>
      <div class="back-brand">QUENDIX</div>
    </section>
  </main>
</body>
</html>
```